Digital One Pager for Consulting Practice

I would like the essence of the content in my ppt consolidated into a one-pager. The one-pager will mainly be sent via email as a pdf and intended to excite and invite new clients and establish the credibility of my boutique high-end consulting firm. Infographics and symbols would be a plus. The target client should view the firm as providing premeir service. The client is getting a thought partner.

Target Market(s)

Large Medical Device Manufacturer Executives, Early-Stage Medical Device Manufacturer Executives, Partners at VC Firms

Industry/Entity Type

Medical Equipment

Colors
0355a3
f37122

Requirements
Must have
• Please match the color scheme in ppt. Please use the existing logo. I am very open to better graphics on the process. My photo does not need to be on the digital flyer. Hyper link to the website and email is needed.
Nice to have
• Infographics

```html
<!DOCTYPE html>
<html lang="en">
<head>
<meta charset="utf-8">
<title>Halvern Ventures — One Pager</title>
<link rel="stylesheet" href="https://fonts.googleapis.com/css2?family=Montserrat:wght@400;600;700;800&family=Open+Sans:wght@400;600;700&display=swap">
<style>
:root{
  --navy:#15223f;
  --navy-deep:#0f1a33;
  --blue:#0355a3;
  --accent:#e2402b;
  --orange:#f37122;
  --ink:#1d2433;
  --grey:#6b7280;
  --light:#f3f4f6;
  --white:#ffffff;
}
*{box-sizing:border-box;margin:0;padding:0}
html,body{width:878px;height:1200px;overflow:hidden;background:var(--white)}
body{font-family:"Open Sans",Arial,sans-serif;color:var(--ink);position:relative}
a{color:inherit;text-decoration:none}

.brand{position:absolute;left:40px;top:30px;display:flex;align-items:center;gap:12px}
.brand-mark{width:26px;height:26px;background:var(--accent);border-radius:50%;flex:none}
.brand-text{display:flex;flex-direction:column;font-family:"Montserrat",sans-serif;color:var(--navy);line-height:1}
.brand-name{font-weight:800;font-size:44px;letter-spacing:1px}
.brand-sub{font-weight:600;font-size:22px;letter-spacing:6px;margin-top:4px}

.portrait{position:absolute;left:440px;top:0;width:438px;height:440px;border-bottom-left-radius:220px;
  background:radial-gradient(circle at 55% 45%,#8a6a55 0,#5a4438 28%,#c9c9cf 52%,#e6e7ea 100%)}

.services{position:absolute;left:38px;top:150px;width:372px;height:410px;background:var(--navy);border-radius:0 0 30px 0;padding:22px 24px}
.services h2{font-family:"Montserrat",sans-serif;font-size:32px;letter-spacing:7px;color:rgba(255,255,255,.2);text-align:center;font-weight:800;margin-bottom:16px}
.service{display:flex;align-items:center;gap:16px;margin-bottom:14px}
.service-photo{flex:none;width:68px;height:68px;border-radius:50%;border:3px solid var(--white);background:linear-gradient(135deg,#9aa3b5,#4d586e)}
.service h3{font-family:"Montserrat",sans-serif;font-size:14px;color:var(--accent);font-weight:700;margin-bottom:4px}
.service li{font-size:11px;color:var(--white);list-style:none;line-height:1.5}
.service li::before{content:"• ";color:var(--orange)}

.offer{position:absolute;left:450px;top:452px;width:405px}
.offer h3{font-family:"Montserrat",sans-serif;font-size:16px;color:var(--accent);font-weight:700;margin:0 0 5px}
.offer ul{margin:0 0 12px 18px;font-size:12px;line-height:1.5}

.process{position:absolute;left:0;top:632px;width:878px;height:250px}
.process-tab{position:absolute;left:0;top:10px;width:62px;height:240px;background:var(--accent);border-radius:0 24px 24px 0;display:flex;align-items:center;justify-content:center}
.process-tab span{transform:rotate(-90deg);white-space:nowrap;font-family:"Montserrat",sans-serif;font-weight:800;color:var(--white);font-size:22px;letter-spacing:1px;line-height:1.05;text-align:center}
.process svg{position:absolute;left:70px;top:0}
.step-label{font-family:"Montserrat",sans-serif;font-size:12px;font-weight:600;fill:var(--ink)}

.partners{position:absolute;left:0;top:888px;width:878px;text-align:center}
.partners-title{display:inline-block;background:var(--accent);color:var(--white);font-family:"Montserrat",sans-serif;font-weight:700;font-size:10px;letter-spacing:1px;padding:4px 18px;border-radius:12px}
.partner-row{display:flex;justify-content:center;gap:26px;margin-top:14px}
.partner-badge{width:120px;height:48px;border-radius:8px;background:var(--light)}
.partner-badge.dark{background:var(--navy)}
.partner-wide{width:260px;height:34px;border-radius:8px;background:var(--light);margin:14px auto 0}

.values{position:absolute;left:0;top:1050px;width:878px;height:44px;background:var(--accent);display:flex;justify-content:space-around;align-items:center;font-family:"Montserrat",sans-serif;font-weight:700;color:var(--white);font-size:17px}
.contact{position:absolute;left:0;top:1094px;width:878px;height:106px;background:var(--navy-deep);display:flex;justify-content:space-around;align-items:center;color:var(--white);font-size:15px}
.contact-item{display:flex;align-items:center;gap:10px}
.contact-icon{width:26px;height:26px;border-radius:50%;background:var(--accent);display:flex;align-items:center;justify-content:center}
</style>
</head>
<body>

<header class="brand">
  <span class="brand-mark"></span>
  <span class="brand-text"><span class="brand-name">HALVERN</span><span class="brand-sub">VENTURES</span></span>
</header>

<div class="portrait" role="img" aria-label="Portrait of the firm's founder in a light shirt and dark blazer"></div>

<section class="services">
  <h2>SERVICES</h2>
  <div class="service">
    <div class="service-photo" role="img" aria-label="Photo of a regulatory strategy meeting"></div>
    <div><h3>Regulatory Strategy</h3><ul><li>FDA/EU Organizational Structure</li><li>Regulatory Pathway</li></ul></div>
  </div>
  <div class="service">
    <div class="service-photo" role="img" aria-label="Photo of a document review session"></div>
    <div><h3>FDA Communications</h3><ul><li>Deficiency Response</li><li>Application Review</li></ul></div>
  </div>
  <div class="service">
    <div class="service-photo" role="img" aria-label="Photo of an executive leader"></div>
    <div><h3>Interim Executive Leadership</h3><ul><li>Compliance Remediation</li><li>Accelerated Product Registration</li></ul></div>
  </div>
  <div class="service">
    <div class="service-photo" role="img" aria-label="Photo of a training workshop"></div>
    <div><h3>Training</h3><ul><li>FDA Communication</li><li>MDR Reporting</li></ul></div>
  </div>
</section>

<section class="offer">
  <h3>Executive Application Review</h3>
  <ul>
    <li>Examples include: Presubmission, IDE, 510(k), 513(g), PMA, Refuse to Accept, Hold letter</li>
    <li>Troubleshooting</li>
  </ul>
  <h3>Strategic Advice &amp; Diligence to Investors</h3>
  <ul>
    <li>Validate &amp; Verify Founder Milestones</li>
    <li>Diligence portfolio company Regulatory and Quality systems</li>
  </ul>
</section>

<section class="process">
  <div class="process-tab"><span>EFFICIENT<br>PROCESS</span></div>
  <svg width="800" height="250" viewBox="0 0 800 250">
    <path d="M20 150 C80 150 90 180 130 170 C220 150 230 100 300 95 C380 90 380 175 460 178 C540 180 560 100 640 95 C700 92 720 140 790 140" fill="none" stroke="var(--accent)" stroke-width="14" stroke-linecap="round"/>
    <g stroke="var(--accent)" stroke-width="4" fill="var(--white)">
      <circle cx="130" cy="170" r="34"/><circle cx="300" cy="95" r="34"/>
      <circle cx="460" cy="178" r="34"/><circle cx="640" cy="95" r="34"/>
    </g>
    <g fill="none" stroke="#8a8f99" stroke-width="2.5" stroke-linecap="round" stroke-linejoin="round">
      <path d="M117 158 l7 -3 l5 10 l-4 3 a18 18 0 0 0 10 10 l3 -4 l10 5 l-3 7 c-14 2 -30 -14 -28 -28z"/>
      <rect x="288" y="78" width="24" height="32" rx="3"/><path d="M294 78 v-4 h12 v4"/><path d="M294 92 l4 4 l8 -8"/>
      <path d="M452 170 a8 8 0 1 1 11 7 v5"/><circle cx="463" cy="190" r="1.2"/>
      <path d="M622 95 q18 -16 36 0 q-18 16 -36 0z"/><circle cx="640" cy="95" r="5"/>
    </g>
    <text class="step-label" x="130" y="228" text-anchor="middle">Exploratory Call</text>
    <text class="step-label" x="300" y="44" text-anchor="middle">Regulatory Landscape</text>
    <text class="step-label" x="460" y="236" text-anchor="middle">Problem Statement</text>
    <text class="step-label" x="640" y="30" text-anchor="middle">Review &amp; Align on</text>
    <text class="step-label" x="640" y="45" text-anchor="middle">Deliverables</text>
  </svg>
</section>

<section class="partners">
  <span class="partners-title">VALUED PARTNER NETWORK</span>
  <div class="partner-row">
    <div class="partner-badge"></div>
    <div class="partner-badge dark"></div>
    <div class="partner-badge"></div>
    <div class="partner-badge"></div>
    <div class="partner-badge"></div>
  </div>
  <div class="partner-wide"></div>
</section>

<div class="values"><span>Extensive Experience</span><span>Efficient Process</span><span>Valued Network</span></div>

<footer class="contact">
  <a class="contact-item" href="https://www.halvernventures.com"><span class="contact-icon"><svg width="14" height="14" viewBox="0 0 14 14" fill="none" stroke="#fff" stroke-width="1.4"><circle cx="7" cy="7" r="6"/><path d="M1 7h12M7 1c3 3 3 9 0 12M7 1c-3 3-3 9 0 12"/></svg></span>www.halvernventures.com</a>
  <span class="contact-item"><span class="contact-icon"><svg width="14" height="14" viewBox="0 0 14 14" fill="#fff"><path d="M3 1l2.5 0.5 1 3-1.5 1a7 7 0 0 0 3.5 3.5l1-1.5 3 1L13 11c0 1-1 2-2 2C6 13 1 8 1 3c0-1 1-2 2-2z"/></svg></span>202.555.0148</span>
  <a class="contact-item" href="mailto:info@halvernventures.com"><span class="contact-icon"><svg width="14" height="14" viewBox="0 0 14 14" fill="none" stroke="#fff" stroke-width="1.4"><rect x="1" y="3" width="12" height="8" rx="1"/><path d="M1 3l6 5 6-5"/></svg></span>info@halvernventures.com</a>
</footer>

</body>
</html>
```